Healthcare/Medical Consultant Company

KTL is a Healthcare Conultant Company. We help doctors manage the business side of their medical practice.
We already have a very basic world press design. We want an upgraded design that conveys partnership, healthcare expertise and healthcare innovation to our client. It needs to have a sleek, clean, modern and inclusive look. Pictures need need to convey diversity (including pictures of people of all races and shows both men and women working together in a healthcare environment to make it better). The Pictures on the home page should particularly illustrate diversity and Healthcare expertise. The company logo is blue and white but the site doesn’t have to follow the exact same theme but the logo needs to blend well with the chosen theme. The logo should ideally be in the header of the website. We would also like the following included in our website:

1. Pages should include: a home page, About Us page, Services page, Get a quote page, Contact Us page, Staff page(where we can add pictures and bio for staff).

2. The Drop down menu for services should have hyperlinks ( for each service)Leading to a page that provides detailed info about that specific service. Our services include: Revenue Cycle Management, Regulatory Compliance, Human Resources Management, & practice Management.

3. Links to social media should in the header or footer of each page.

4. Contact info should be in the footer of each page.

5. Clients should be an email to us from the contact page.

Target Market(s)

Physician Medical Practices

Industry/Entity Type

Medical

Coding

Coded - Design and coding required

Font styles to use
Sans Serif

Colors

Designer to choose colors to be used in the design.

Requirements
Must have
• See project description
Nice to have
• See project description

```html
<!DOCTYPE html>
<html lang="en">
<head>
<meta charset="utf-8">
<title>KTL Health Partners</title>
<link href="https://fonts.googleapis.com/css2?family=Roboto+Slab:wght@400;700&family=Roboto:wght@400;500&display=swap" rel="stylesheet">
<style>
:root{
  --blue:#1d5fb0;
  --blue-dark:#123f86;
  --blue-light:#2e86d0;
  --sky:#e3f1fb;
  --ink:#2b2b2b;
  --muted:#555;
  --grey:#efefef;
  --dark:#1b1b1b;
  --white:#fff;
}
*{box-sizing:border-box;margin:0;padding:0}
html,body{width:1200px;height:3696px;overflow:hidden}
body{font-family:'Roboto',sans-serif;color:var(--ink);background:var(--white);position:relative}
h1,h2,h3,h4{font-family:'Roboto Slab',serif}
.section{position:relative;width:1200px;overflow:hidden}
.abs{position:absolute}

/* header */
.site-header{height:106px}
.brand{left:122px;top:14px;text-align:center;color:var(--blue-dark)}
.brand-mark{font-family:'Roboto Slab',serif;font-weight:700;font-size:46px;line-height:50px;letter-spacing:2px}
.brand-name{font-family:'Roboto Slab',serif;font-size:13px;line-height:16px}
.main-nav{left:436px;top:62px;display:flex;gap:30px;font-family:'Roboto Slab',serif;font-size:19px;color:#333}
.call{left:676px;top:20px;font-family:'Roboto Slab',serif;font-size:18px;color:#333;display:flex;align-items:center;gap:8px}
.btn-pill{display:inline-block;background:var(--blue-light);color:var(--white);border-radius:22px;font-family:'Roboto Slab',serif}
.quote-btn{left:925px;top:15px;width:142px;height:36px;line-height:36px;text-align:center;font-size:17px}

/* hero */
.hero{height:621px}
.hero-photo{inset:0;background:linear-gradient(100deg,#2a6fb6 0%,#6fa6d6 35%,#cfdbe6 60%,#e8eef3 100%)}
.hero-title{left:0;width:1200px;top:370px;text-align:center;color:var(--white);font-size:46px;line-height:60px;font-weight:700;text-shadow:0 2px 6px rgba(0,0,0,.25)}
.hero-cta{left:497px;top:514px;width:226px;height:44px;line-height:44px;text-align:center;font-size:18px;font-weight:700;background:var(--blue)}
.arrow{width:32px;height:32px;border-radius:50%;background:rgba(40,40,40,.75);top:384px}
.hero-curve{left:0;bottom:0}

/* about */
.about{height:468px}
.about-photo{left:137px;top:30px;width:350px;height:350px;border-radius:50%;border:6px solid var(--white);box-shadow:0 0 0 5px var(--blue-light);background:radial-gradient(circle at 55% 45%,#8fb3d6,#1f4f85 70%)}
.about-text{left:530px;top:50px;width:565px}
.about-text h2{font-size:38px;color:#222;margin-bottom:22px}
.about-text p{font-size:13.5px;line-height:28px;color:#333}
.btn-outline{display:inline-block;margin-top:20px;border:2px solid #333;border-radius:20px;padding:6px 18px;font-family:'Roboto Slab',serif;font-size:13px;color:#222}

/* services */
.services{height:579px;background:linear-gradient(180deg,#1e63bd,#1a55a8)}
.services h2{position:absolute;top:86px;width:1200px;text-align:center;color:var(--white);font-size:37px}
.svc-card{top:240px;width:302px;height:230px;background:var(--white);border:1px solid #d0d8e4;text-align:center;padding:72px 16px 0}
.svc-icon{position:absolute;left:101px;top:-50px;width:100px;height:100px;border-radius:50%;background:var(--blue-light);border:7px solid var(--white)}
.svc-icon svg{margin-top:22px}
.svc-card h3{font-size:18px;line-height:24px;color:var(--blue-dark);margin-bottom:10px}
.svc-card p{font-size:12.5px;line-height:21px;color:#444;height:63px;overflow:hidden}

/* consultant */
.consult{height:468px;background:linear-gradient(90deg,#f4f8fb,var(--sky))}
.consult-photo{left:0;top:0;width:640px;height:468px;background:linear-gradient(90deg,#d9e3ea,#b7c7d6 60%,#dce9f4)}
.consult-text{left:685px;top:72px;width:440px}
.consult-text h2{font-size:39px;line-height:48px;font-weight:400;color:#222;margin-bottom:20px}
.consult-text p{font-size:13.5px;line-height:27px;color:#333}
.btn-square{display:inline-block;margin-top:22px;background:var(--blue-light);color:var(--white);padding:8px 18px;font-family:'Roboto Slab',serif;font-size:13px;border-radius:3px}

/* blogs */
.blogs{height:550px}
.blogs h2{position:absolute;top:78px;width:1200px;text-align:center;font-size:37px;color:#222}
.post{top:178px;width:292px}
.post-img{height:185px;background:linear-gradient(135deg,#c9d2da,#7b8ea3)}
.post-img.warm{background:linear-gradient(135deg,#e3d9cc,#9a7f5e)}
.post-img.light{background:linear-gradient(135deg,#eef1f4,#a9b8c7)}
.post-meta{margin-top:22px;border-left:5px solid var(--blue-light);padding-left:16px}
.post-date{font-size:14px;color:var(--blue-dark);display:flex;align-items:center;gap:7px}
.post-title{margin-top:10px;font-size:15.5px;line-height:24px;color:var(--blue)}

/* testimonials */
.clients{height:473px}
.clients-bg{inset:0;background:linear-gradient(180deg,#262626,#121212)}
.clients h2{position:absolute;top:82px;width:1200px;text-align:center;font-size:30px;color:var(--white)}
.quote{top:180px;width:320px;display:flex;gap:22px}
.avatar{flex:none;width:72px;height:72px;border-radius:50%;border:3px solid var(--white);background:linear-gradient(135deg,#b99b86,#5b4a40)}
.quote p{font-size:12.5px;line-height:21px;color:#ddd}
.quote p b{font-family:'Roboto Slab',serif;font-size:22px;color:var(--white);margin-right:6px}
.quote .who{margin-top:8px;font-style:italic;font-size:12.5px;line-height:24px;color:var(--blue-light)}
.dots{top:370px;left:566px;display:flex;gap:9px}
.dots span{width:9px;height:9px;border-radius:50%;background:var(--white)}
.dots span.on{box-shadow:0 0 0 3px #1b1b1b,0 0 0 5px var(--white)}

/* footer */
.site-footer{height:431px;background:var(--grey)}
.site-footer h4{font-size:20px;color:#222;margin-bottom:22px}
.quick{left:132px;top:60px}
.quick li{list-style:none;font-size:13px;line-height:24px;color:#333}
.quick li::before{content:"›";margin-right:14px;color:#666}
.contact{left:335px;top:60px}
.contact-row{display:flex;gap:10px;font-size:13.5px;line-height:19px;color:#222;margin-bottom:14px}
.social{display:flex;gap:5px;margin-top:22px}
.social span{width:22px;height:22px;border-radius:50%;border:1.5px solid var(--blue)}
.quote-form{left:630px;top:60px;width:438px}
.form-grid{display:grid;grid-template-columns:210px 210px;gap:10px 18px}
.field{height:40px;background:var(--white);border:1px solid #ccc;font-size:11px;color:#555;padding:12px 12px}
.submit{width:210px;height:40px;margin-top:16px;background:var(--blue-light);color:var(--white);text-align:center;line-height:40px;font-size:13px;font-weight:500}
.legal{left:132px;top:340px;width:936px;border-top:1px solid #ccc;padding-top:38px;text-align:center;font-size:12.5px;color:#333}
</style>
</head>
<body>

<header class="section site-header">
  <div class="abs brand">
    <div class="brand-mark">KTL</div>
    <div class="brand-name">KTL Health Partners LLC</div>
  </div>
  <div class="abs call">
    <svg width="18" height="18" viewBox="0 0 24 24"><path fill="#2e86d0" d="M6.6 10.8a15 15 0 0 0 6.6 6.6l2.2-2.2c.3-.3.7-.4 1-.2 1.1.4 2.3.6 3.6.6.6 0 1 .4 1 1V20c0 .6-.4 1-1 1A17 17 0 0 1 3 4c0-.6.4-1 1-1h3.5c.6 0 1 .4 1 1 0 1.3.2 2.5.6 3.6.1.3 0 .7-.2 1z"/></svg>
    Call Us 0800 555 010
  </div>
  <span class="abs btn-pill quote-btn">Get a quote</span>
  <nav class="abs main-nav">
    <span>Home</span><span>About Us</span><span>Services</span><span>Get a quote</span><span>Contact Us</span><span>Staff</span>
  </nav>
</header>

<section class="section hero">
  <div class="abs hero-photo" role="img" aria-label="Photo of a diverse team of doctors and nurses talking together in a bright hospital"></div>
  <h1 class="abs hero-title">KTL Health Partners<br>Advancing Healthcare</h1>
  <span class="abs btn-pill hero-cta">make an appointment</span>
  <span class="abs arrow" style="left:97px"><svg width="32" height="32"><path d="M19 10l-6 6 6 6" stroke="#fff" stroke-width="2.5" fill="none"/></svg></span>
  <span class="abs arrow" style="left:1069px"><svg width="32" height="32"><path d="M13 10l6 6-6 6" stroke="#fff" stroke-width="2.5" fill="none"/></svg></span>
  <svg class="abs hero-curve" width="1200" height="120" viewBox="0 0 1200 120">
    <path d="M0 56 Q600 -40 1200 56 L1200 120 L0 120Z" fill="#fff"/>
    <path d="M40 108 Q600 -10 1160 108" stroke="#123f86" stroke-width="5" fill="none"/>
  </svg>
</section>

<section class="section about">
  <div class="abs about-photo" role="img" aria-label="Photo of a surgeon in a cap looking at a floating medical technology interface"></div>
  <div class="abs about-text">
    <h2>ABOUT US</h2>
    <p>KTL Health Partners (KTL) is a healthcare consulting firm skilled at helping physician practices advance their strategic vision in an ever-evolving healthcare system. KTL Health Partners specializes in revenue cycle optimization, practice management improvement and developing new physician practices. Our technical skills allow us to dig deep into your revenue cycle while our strategic approach ensures we're keeping our eyes on the entire financial picture.</p>
    <span class="btn-outline">READ MORE</span>
  </div>
</section>

<section class="section services">
  <h2>KTL SERVICES</h2>
  <div class="abs svc-card" style="left:130px">
    <div class="svc-icon"><svg width="46" height="46" viewBox="0 0 46 46" fill="none" stroke="#fff" stroke-width="2.5"><path d="M23 42V20M23 28l-9-8M23 24l9-8M12 10h3M31 8h3M22 6h3"/></svg></div>
    <h3>REVENUE CYCLE<br>MANAGEMENT</h3>
    <p>In today's increasingly complex health care environment it's important now more than ever that medical practices closely manage their revenue cycle. Partners</p>
  </div>
  <div class="abs svc-card" style="left:449px">
    <div class="svc-icon"><svg width="46" height="46" viewBox="0 0 46 46" fill="none" stroke="#fff" stroke-width="2.5"><rect x="6" y="8" width="34" height="24" rx="2"/><path d="M23 14v12M17 20h12M16 40h14M23 32v8"/></svg></div>
    <h3>REGULATORY &amp;<br>COMPLIANCE MANAGEMENT</h3>
    <p>In a heavily regulated healthcare environment medical practices need to be acutely aware of regulations as they present huge liabilities. It is extremely important to ensure</p>
  </div>
  <div class="abs svc-card" style="left:768px">
    <div class="svc-icon"><svg width="46" height="46" viewBox="0 0 46 46" fill="none" stroke="#fff" stroke-width="2.5"><rect x="10" y="6" width="24" height="32" rx="2"/><path d="M16 14h12M16 20h12M16 26h7M30 30l8 8"/></svg></div>
    <h3>PRACTICE<br>MANAGEMENT</h3>
    <p>Practice Management is challenging and it requires the right balance of skill, knowledge, experience and management expertise. KTL Offers assessment and optimization</p>
  </div>
</section>

<section class="section consult">
  <div class="abs consult-photo" role="img" aria-label="Photo of a smiling female doctor with a stethoscope, colleagues working behind her"></div>
  <div class="abs consult-text">
    <h2>Healthcare &amp; Medical<br>Consultant</h2>
    <p>Sed ut perspiciatis unde omnis iste natus error sit voluptatem aantium doloremque laudantium, totam rem aperiam, eaque ipsa quae ab illo inventore veritatis et quasi architecto beatae vitae dicta sunt explibo. Nemo enim ipsam voluptatem quia voluptas sit aspernatur aut odit aut fugit, sed quia consequuntur magni</p>
    <span class="btn-square">READ MORE</span>
  </div>
</section>

<section class="section blogs">
  <h2>LATEST BLOGS</h2>
  <article class="abs post" style="left:130px">
    <div class="post-img" role="img" aria-label="Photo of a group of doctors in scrubs discussing in a corridor"></div>
    <div class="post-meta">
      <div class="post-date"><svg width="12" height="12" viewBox="0 0 12 12"><rect x="1" y="2" width="10" height="9" fill="#123f86"/><rect x="2" y="5" width="8" height="5" fill="#fff"/></svg>October 17, 2018</div>
      <div class="post-title">Sed ut perspiciatis unde omnis iste sit voluptatem accusantium</div>
    </div>
  </article>
  <article class="abs post" style="left:451px">
    <div class="post-img light" role="img" aria-label="Photo of a doctor writing notes at a desk with a stethoscope"></div>
    <div class="post-meta">
      <div class="post-date"><svg width="12" height="12" viewBox="0 0 12 12"><rect x="1" y="2" width="10" height="9" fill="#123f86"/><rect x="2" y="5" width="8" height="5" fill="#fff"/></svg>October 17, 2018</div>
      <div class="post-title">Sed ut perspiciatis unde omnis iste sit voluptatem accusantium</div>
    </div>
  </article>
  <article class="abs post" style="left:773px">
    <div class="post-img warm" role="img" aria-label="Photo of a consultant meeting with a couple at a table"></div>
    <div class="post-meta">
      <div class="post-date"><svg width="12" height="12" viewBox="0 0 12 12"><rect x="1" y="2" width="10" height="9" fill="#123f86"/><rect x="2" y="5" width="8" height="5" fill="#fff"/></svg>October 17, 2018</div>
      <div class="post-title">Sed ut perspiciatis unde omnis iste sit voluptatem accusantium</div>
    </div>
  </article>
</section>

<section class="section clients">
  <div class="abs clients-bg" role="img" aria-label="Darkened photo of a medical team in a hospital"></div>
  <h2>WHAT OUR CLIENTS SAY</h2>
  <div class="abs quote" style="left:130px">
    <div class="avatar" role="img" aria-label="Client portrait"></div>
    <div><p><b>“</b>At vero eos et accusamus et iustodio dignissimos ducimus qui blanditiispraesent ium voluptatum deleniti atque corrupos</p><div class="who">Jordan Hale<br>KTL Health Partners</div></div>
  </div>
  <div class="abs quote" style="left:458px">
    <div class="avatar" role="img" aria-label="Client portrait"></div>
    <div><p><b>“</b>At vero eos et accusamus et iustodio dignissimos ducimus qui blanditiispraesent ium voluptatum deleniti atque corrupos</p><div class="who">Jordan Hale<br>KTL Health Partners</div></div>
  </div>
  <div class="abs quote" style="left:798px">
    <div class="avatar" role="img" aria-label="Client portrait"></div>
    <div><p><b>“</b>At vero eos et accusamus et iustodio dignissimos ducimus qui blanditiispraesent ium voluptatum deleniti atque corrupos</p><div class="who">Jordan Hale<br>KTL Health Partners</div></div>
  </div>
  <div class="abs dots"><span class="on"></span><span></span><span></span><span></span></div>
</section>

<footer class="section site-footer">
  <div class="abs quick">
    <h4>QUICK LINK</h4>
    <ul><li>Home</li><li>About Us</li><li>Services</li><li>Get a quote</li><li>Staff</li><li>Contact</li></ul>
  </div>
  <div class="abs contact">
    <h4>CONTACT US</h4>
    <div class="contact-row"><svg width="12" height="16" viewBox="0 0 12 16"><path d="M6 0a6 6 0 0 1 6 6c0 4-6 10-6 10S0 10 0 6a6 6 0 0 1 6-6z" fill="#2e86d0"/><circle cx="6" cy="6" r="2" fill="#fff"/></svg><span>KTL Health Partners<br>Brookfield Falls, CT 06000</span></div>
    <div class="contact-row"><svg width="14" height="14" viewBox="0 0 24 24"><path fill="#2e86d0" d="M6.6 10.8a15 15 0 0 0 6.6 6.6l2.2-2.2c.3-.3.7-.4 1-.2 1.1.4 2.3.6 3.6.6.6 0 1 .4 1 1V20c0 .6-.4 1-1 1A17 17 0 0 1 3 4c0-.6.4-1 1-1h3.5c.6 0 1 .4 1 1 0 1.3.2 2.5.6 3.6.1.3 0 .7-.2 1z"/></svg><span>Phone: (888) 555-0147<br>(888) 555-0147</span></div>
    <div class="contact-row"><svg width="14" height="12" viewBox="0 0 14 12"><rect width="14" height="12" fill="#2e86d0"/><path d="M0 0l7 6 7-6" stroke="#fff" fill="none"/></svg><span>info@ktlhealth.example</span></div>
    <div class="social"><span></span><span></span><span></span><span></span></div>
  </div>
  <div class="abs quote-form">
    <h4>GET A QUOTE</h4>
    <div class="form-grid">
      <div class="field">Your Name</div><div class="field">Your E - Mail</div>
      <div class="field">Your Phone</div><div class="field">Message</div>
    </div>
    <div class="submit">SUBMIT</div>
  </div>
  <div class="abs legal">©2018 KTL Health Partners. All Rights Reserved. Disclaimer &nbsp;|&nbsp; Privacy policy &nbsp;|&nbsp; Terms of use</div>
</footer>

</body>
</html>
```